Dorsey K. Wendell Business Card

We need a business card for our company Dorsey K. Wendell Heating & Plumbing to be distributed to potential customers. It should follow the color scheme of our logo and have a modern upscale and masculine look.

The logo is attached and the info below should also be included:

5187 W. Cedar Brook Rd.
Larkfield, PA 17832

Russell T. Wendell
(717) 592-0817
russelltwendell@fernmail.net
dorseykwendell.net
PA #093148

Industry/Entity Type

Business

Contact Information for Business Card

5187 W. Cedar Brook Rd.
Larkfield, PA 17832

Russell T. Wendell
(717) 592-0817
russelltwendell@fernmail.net
dorseykwendell.net
PA #093148

Colors

Designer to choose colors to be used in the design.

Requirements
Must have
• Information above included

```html
<!DOCTYPE html>
<html lang="en">
<head>
<meta charset="UTF-8">
<title>Dorsey K. Wendell Business Card</title>
<link rel="stylesheet" href="https://fonts.googleapis.com/css2?family=Montserrat:wght@700;800&family=Questrial&display=swap">
<style>
  :root {
    --backdrop: #1d1d1f;
    --brand-blue: #0f5aa6;
    --brand-green: #9fcb3b;
    --paper: #ffffff;
  }
  * { margin: 0; padding: 0; box-sizing: border-box; }
  html, body { width: 1200px; height: 800px; overflow: hidden; }
  body {
    background: var(--backdrop);
    font-family: "Questrial", Arial, sans-serif;
    position: relative;
  }
  .card {
    position: absolute;
    width: 540px;
    height: 310px;
    overflow: hidden;
    background: var(--paper);
    box-shadow: 0 10px 30px rgba(0,0,0,.45);
  }
  .card-front { left: 40px; top: 245px; }
  .card-back { left: 620px; top: 245px; }
  .card-art { position: absolute; inset: 0; }

  .front-brand {
    position: absolute;
    left: 26px; top: 30px;
    display: flex; align-items: center; gap: 7px;
    font-family: "Montserrat", Arial, sans-serif;
    font-weight: 800;
    font-size: 15px;
    color: var(--brand-blue);
    letter-spacing: .3px;
  }
  .brand-square {
    width: 20px; height: 20px;
    background: var(--brand-blue);
  }
  .name-pill {
    position: absolute;
    right: 0; top: 40px;
    height: 38px;
    padding: 0 26px 0 24px;
    background: var(--brand-blue);
    border-radius: 19px 0 0 19px;
    color: var(--paper);
    font-family: "Montserrat", Arial, sans-serif;
    font-weight: 700;
    font-size: 19px;
    line-height: 38px;
  }
  .contact-list {
    position: absolute;
    left: 34px; top: 188px;
    color: var(--paper);
    font-size: 14px;
    line-height: 19px;
    list-style: none;
  }
  .contact-list .address { margin-top: 10px; }

  .back-brand {
    position: absolute;
    left: 0; right: 0; top: 125px;
    display: flex; justify-content: center; align-items: center; gap: 12px;
    font-family: "Montserrat", Arial, sans-serif;
    font-weight: 800;
    font-size: 30px;
    color: var(--brand-blue);
    letter-spacing: .5px;
  }
  .back-brand .brand-square { width: 42px; height: 42px; }
</style>
</head>
<body>

<section class="card card-front" aria-label="Business card front">
  <svg class="card-art" viewBox="0 0 540 310" width="540" height="310" aria-hidden="true">
    <path d="M0 168 C 140 150, 330 165, 540 68 L540 310 L0 310 Z" fill="var(--brand-green)"/>
    <path d="M0 180 C 150 160, 340 170, 540 80 L540 310 L0 310 Z" fill="var(--brand-blue)"/>
  </svg>
  <div class="front-brand"><span class="brand-square"></span>Dorsey K. Wendell</div>
  <div class="name-pill">Russell T. Wendell</div>
  <ul class="contact-list">
    <li>(717) 592-0817</li>
    <li>russelltwendell@fernmail.net</li>
    <li>dorseykwendell.net</li>
    <li>PA #093148</li>
    <li class="address">5187 W. Cedar Brook Rd., Larkfield, PA 17832</li>
  </ul>
</section>

<section class="card card-back" aria-label="Business card back">
  <svg class="card-art" viewBox="0 0 540 310" width="540" height="310" aria-hidden="true">
    <rect width="540" height="310" fill="var(--brand-blue)"/>
    <rect y="82" width="540" height="146" fill="var(--brand-green)"/>
    <rect y="88" width="540" height="134" fill="var(--paper)"/>
  </svg>
  <div class="back-brand"><span class="brand-square"></span>Dorsey K. Wendell</div>
</section>

</body>
</html>
```